New Website Design (Uncoded) Competition for Velto Trade Link

Please submit design concepts for a Joomla 3.0 Website for VELTO TRADE LINK company. Our client prefers a modem style design, responsive to all mobile devices,
The website demo content needs to be clear and detailed.

Menu sample:
Home/About Us/Service/Strength/Partner/News/Contact US/Blog

Requirements:
1. Only need to submit the PSD for the design, coding work is not included.
2. Please submit both Homepage and Inner page to demonstrate the concept.
3. The Homepage needs to include: LOGO/MENU/Banner/Language Switcher/Company Introduction/Welcome module/Advertising Module/Footer Menu/Footer/Copyright/Social Links
4. Use Asian business women for demo pictures/Could try city pictures for background.
5. Prefer SINGLE SCREEN design rather than scrollable multiple screen designs.
6. Avoid any chain symbol since the company is more about financial business.
7. Avoid any direct connotations related with money or cash.
Updates

Hi Designers, I have clearly state the requirements that avoid using neg connontation pictures like cash/ property, though still receive concepts like that. Please check the brief clearly and mark at Update with "cheers" Kip from LW

Target Market(s)

Shenzhen Dorvik Velto Trade link Company provide cross-border Supply chain Financial service by integrating Dorvik Trade Link resource.
The Company mission is become the most respectful, professional and valuable Chinese Supply Chain Financial Company, pioneer the supply chain industry.

Industry/Entity Type

Financial

Font styles to use
Sans Serif

Colors
33b7a4

Requirements
Must have
• 1. Necessary Web element, including Logo/navigation/ Banner/ Footer
2. Asia business Women pictures.
Should not have
• 6. Avoid any chain symbol since the company is more about financial business.

```html
<!DOCTYPE html>
<html lang="en">
<head>
<meta charset="utf-8">
<title>Velto Trade Link</title>
<link href="https://fonts.googleapis.com/css2?family=Figtree:wght@400;500;600;700;800&display=swap" rel="stylesheet">
<style>
:root{
  --ink:#333438;
  --text:#4a4a4a;
  --muted:#9a9a9a;
  --blue:#1f7fc4;
  --blue-dark:#1a6fae;
  --black:#0a0a0a;
  --dark-btn:#343438;
  --footer-bg:#ececef;
  --line:#d0d0d4;
  --panel-top:#ffffff;
  --panel-bottom:#dedede;
}
*{box-sizing:border-box;margin:0;padding:0}
html,body{width:1107px;height:1200px;overflow:hidden}
body{position:relative;background:#fff;font-family:"Figtree",Arial,sans-serif;color:var(--text)}
a{text-decoration:none;color:inherit}
.abs{position:absolute}

.topbar{left:0;top:0;width:1107px;height:30px;background:var(--black);color:#fff;font-size:13px}
.topbar .account{position:absolute;right:101px;top:7px}
.topbar .account span{margin:0 6px;color:#aaa}

.page{left:101px;top:30px;width:905px;height:1130px;background:#fff;box-shadow:0 0 6px rgba(0,0,0,.25)}

.header{left:101px;top:30px;width:905px;height:113px;background:#fff}
.brand{left:20px;top:28px;display:flex;align-items:center;gap:10px}
.brand-dot{width:44px;height:44px;border-radius:50%;background:var(--blue)}
.brand-name{font-size:25px;font-weight:800;color:#555;letter-spacing:.5px;line-height:1}
.sales{right:307px;top:25px;font-size:13.5px;color:var(--ink)}
.search{left:607px;top:16px;width:278px;height:30px;border:1px solid #dcdcdc;border-radius:3px;background:#fff;box-shadow:inset 0 1px 2px rgba(0,0,0,.06)}
.search .placeholder{position:absolute;left:10px;top:7px;font-size:11.5px;color:#aaa}
.search .btn{position:absolute;right:2px;top:2px;width:32px;height:24px;border:1px solid #d8d8d8;border-radius:3px;background:linear-gradient(#fafafa,#e6e6e6)}
.nav{right:19px;top:76px;display:flex;gap:31.5px;font-size:13.5px;color:var(--ink)}
.nav .active{color:var(--blue)}

.hero{left:0;top:143px;width:1107px;height:410px;background:linear-gradient(100deg,#cfe6ef 0%,#a9d6e6 25%,#e4eff3 55%,#d9eaf0 80%,#b9dbe8 100%)}
.hero-photo{left:517px;top:143px;width:544px;height:410px;background:linear-gradient(160deg,#e9eef1 0%,#f4f4f4 45%,#2d5fb3 85%,#3f6fc2 100%);opacity:.9}
.hero-copy{left:122px;top:203px;width:430px}
.hero-copy h1{font-weight:400;font-size:41px;line-height:50px;color:var(--ink)}
.hero-copy h1 .accent{color:var(--blue);font-weight:800}
.hero-copy p{margin-top:12px;font-size:12.5px;line-height:22px;color:#555}
.hero-actions{left:122px;top:394px;display:flex;gap:28px}
.button{display:block;width:137px;height:41px;border-radius:3px;color:#fff;font-size:16px;text-align:center;line-height:41px}
.button.primary{background:var(--blue)}
.button.secondary{background:var(--dark-btn)}

.services{left:121px;top:517px;width:867px;height:271px;border:1px solid #c9c9c9;background:linear-gradient(var(--panel-top),var(--panel-bottom))}
.service{position:absolute;top:17px;width:193px}
.service .thumb{width:193px;height:115px}
.service h3{margin-top:21px;font-size:16.5px;font-weight:500;color:var(--ink)}
.service p{margin-top:10px;padding-left:1px;font-size:11.5px;line-height:16.6px;color:#333}
.service .more{display:inline-block;margin-top:10px;margin-left:3px;font-size:11.5px;color:var(--blue);text-decoration:underline}

.partners{left:101px;top:816px;width:905px;height:74px}
.partner{position:absolute;top:0;height:74px;display:flex;align-items:center;justify-content:center;gap:7px;font-size:16px;font-weight:700;color:#555}
.partner .mark{width:14px;height:14px;border-radius:50%}
.partner + .partner{border-left:1px solid #e2e2e2}

.footer{left:101px;top:935px;width:905px;height:225px;background:var(--footer-bg)}
.pin{left:427px;top:-33px;width:66px;height:66px;border-radius:50%;background:#fff;display:flex;align-items:center;justify-content:center}
.footer-col{position:absolute;top:62px;width:110px}
.footer-col h4{font-size:14.5px;font-weight:400;color:#555;padding-bottom:7px;border-bottom:1px solid #b9b9bd;margin-bottom:8px}
.footer-col li{list-style:none;font-size:12px;color:#8e8e8e;line-height:24px;padding-left:1px}
.footer-divider{left:643px;top:65px;width:1px;height:125px;background:var(--line)}
.contact{left:681px;top:60px;font-size:12px;color:#8e8e8e;line-height:21.3px}
.social{left:679px;top:150px;display:flex;gap:11px}
.social span{display:block;width:30px;height:30px;border-radius:50%;background:#cdcdd0}

.bottombar{left:0;top:1160px;width:1107px;height:40px;background:var(--black);font-size:12px;color:#c8c8c8}
.bottombar .copy{position:absolute;left:121px;top:13px}
.bottombar .legal{position:absolute;right:120px;top:13px}
.bottombar .legal span{margin:0 9px;color:#888}
</style>
</head>
<body>

<div class="abs topbar"><div class="account"><a href="#">Login</a><span>|</span><a href="#">Signup</a></div></div>

<div class="abs hero"></div>
<div class="abs hero-photo" role="img" aria-label="Photo of a smiling Asian businesswoman at a desk in a bright office"></div>

<div class="abs page" style="height:113px;box-shadow:none;background:transparent"></div>

<header class="abs header">
  <div class="abs brand"><span class="brand-dot"></span><span class="brand-name">VELTO TRADE LINK</span></div>
  <div class="abs sales">Sales Team: + 100 555 02478</div>
  <div class="abs search">
    <span class="placeholder">Search...</span>
    <span class="btn">
      <svg width="30" height="22" viewBox="0 0 30 22"><circle cx="14" cy="10" r="3.6" fill="none" stroke="#333" stroke-width="1.6"/><line x1="16.6" y1="12.6" x2="19" y2="15" stroke="#333" stroke-width="1.8"/></svg>
    </span>
  </div>
  <nav class="abs nav">
    <a class="active" href="#">Home</a><a href="#">About Us</a><a href="#">Service</a><a href="#">Strength</a><a href="#">Partner</a><a href="#">News</a><a href="#">Contact Us</a><a href="#">Blog</a>
  </nav>
</header>

<section class="abs hero-copy">
  <h1>Welcome To<br><span class="accent">VELTO</span> Trade Link</h1>
  <p>Lorem ipsum dolor sit amet, consectetur adipiscing elit. Integer auctor lectus ut euismod bibendum. Morbi id varius ligula, vitae molestie justo. Mauris ac ipsum ante.</p>
</section>
<div class="abs hero-actions">
  <a class="button primary" href="#">Learn More</a>
  <a class="button secondary" href="#">Contact Us</a>
</div>

<section class="abs services">
  <article class="service" style="left:22px">
    <div class="thumb" role="img" aria-label="Photo of a container port at dusk with cranes" style="background:linear-gradient(#3c5f95,#6a6e7a 55%,#8a5a3a)"></div>
    <h3>International Logistics</h3>
    <p>Lorem ipsum dolor sit amet, consec-tetur adipiscing elit. Integer auctor lectus ut euismod...</p>
    <a class="more" href="#">Read more...</a>
  </article>
  <article class="service" style="left:232px">
    <div class="thumb" role="img" aria-label="Photo of a white truck on a highway" style="background:linear-gradient(135deg,#5a3d1a,#c98a2c 50%,#6e4a1c)"></div>
    <h3>Contract Logistics</h3>
    <p>Lorem ipsum dolor sit amet, consec-tetur adipiscing elit. Integer auctor lectus ut euismod...</p>
    <a class="more" href="#">Read more...</a>
  </article>
  <article class="service" style="left:443px">
    <div class="thumb" role="img" aria-label="Photo of a container ship at sea" style="background:linear-gradient(#2a4a6a,#1c3550)"></div>
    <h3>Distribution Across Asia</h3>
    <p>Lorem ipsum dolor sit amet, consec-tetur adipiscing elit. Integer auctor lectus ut euismod...</p>
    <a class="more" href="#">Read more...</a>
  </article>
  <article class="service" style="left:653px">
    <div class="thumb" role="img" aria-label="Photo of colourful shirts on a clothing rack" style="background:linear-gradient(90deg,#b94a7a,#6cb4d8 40%,#e7e0e6 70%,#c45a9a)"></div>
    <h3>Value Added Services</h3>
    <p>Lorem ipsum dolor sit amet, consec-tetur adipiscing elit. Integer auctor lectus ut euismod...</p>
    <a class="more" href="#">Read more...</a>
  </article>
</section>

<section class="abs partners">
  <div class="partner" style="left:0;width:165px"><span class="mark" style="background:#3aaa3a"></span>Fernway</div>
  <div class="partner" style="left:165px;width:187px"><span class="mark" style="background:#8bc53f"></span>Brisko</div>
  <div class="partner" style="left:352px;width:188px"><span class="mark" style="background:#d7263d"></span>Halden Marine</div>
  <div class="partner" style="left:540px;width:187px"><span class="mark" style="background:#f5a800"></span>Tovaline</div>
  <div class="partner" style="left:727px;width:178px"><span class="mark" style="background:#d71920"></span>Orbisa</div>
</section>

<footer class="abs footer">
  <div class="abs pin">
    <svg width="20" height="26" viewBox="0 0 20 26"><path d="M10 1C5.2 1 2 4.5 2 8.8 2 14.5 10 24 10 24s8-9.5 8-15.2C18 4.5 14.8 1 10 1z" fill="none" stroke="#c4c4c8" stroke-width="1.5"/><circle cx="10" cy="9" r="3" fill="none" stroke="#c4c4c8" stroke-width="1.5"/></svg>
  </div>
  <div class="footer-col" style="left:28px"><h4>VELTO</h4><ul><li>Home</li><li>Download</li><li>Apps</li></ul></div>
  <div class="footer-col" style="left:176px"><h4>ABOUT US</h4><ul><li>About velto</li><li>Company</li><li>Privacy</li><li>Press</li></ul></div>
  <div class="footer-col" style="left:334px"><h4>COMMUNITY</h4><ul><li>Blog</li><li>Support</li><li>Translation Tool</li><li>Developer</li></ul></div>
  <div class="footer-col" style="left:494px"><h4>SUPPORT US</h4><ul><li>Knowledgebase</li><li>Download &amp; Update</li><li>Information</li><li>Documentation</li></ul></div>
  <div class="abs footer-divider"></div>
  <address class="abs contact" style="font-style:normal">Shenzhen Dorvik<br>88 Linwe Road, Suite 310,<br>Shenzhen Dorvik, ZD 50817<br>(100) 555-0193 International</address>
  <div class="abs social" aria-label="Social links"><span></span><span></span><span></span></div>
</footer>

<div class="abs bottombar">
  <div class="copy">Copyrights © 2014- All Rights Reserved</div>
  <div class="legal"><a href="#">Privacy Policy</a><span>|</span><a href="#">Terms &amp; Condition</a></div>
</div>

</body>
</html>
```